Business Card Design

We have a group of different function companies owned and operated by one person. We are located in the Dallas Fort Worth area in Texas. We develop properties to where we are owners and develop properties that are not ours as well. We build custom homes and commercial buildings. We also do residential and commercial remodeling. We also own commercial properties in which we lease office space. We are trying to merge all we do into one card and have done so already into one website. We initially had thought of having a logo made with HV in nice attractive lettering maybe as a watermark. We are open to the color scheme but no neons or pastels.

Project Deadline Extended
Reason: I am needing 2 different cards for two businesses.

Industry/Entity Type

Residential

Contact Information for Business Card

Harwell Ventures
4826 Mabry Ln. Suite 417
Keller, Texas 76109
Land Development
Residential and Commercial Construction
Commercial Real Estate
Dale Wintermoot
www.harwellgrp.example
dale@harwellgrp.example
Cell: 817-555-0142
Office: 817-555-0187
Fax: 8175550163

```html
<!DOCTYPE html>
<html lang="en">
<head>
<meta charset="utf-8">
<title>Harwell Ventures — Business Card</title>
<link href="https://fonts.googleapis.com/css2?family=Tinos:wght@400;700&family=Arimo:wght@400&display=swap" rel="stylesheet">
<style>
  :root {
    --backdrop: #e9e6e1;
    --band-top: #6b6b6b;
    --band-bottom: #5a5a5a;
    --peach: #f2b896;
    --white: #ffffff;
    --ink: #111111;
    --accent-green: #5fbf3a;
    --serif: "Tinos", "Times New Roman", serif;
    --sans: "Arimo", Arial, sans-serif;
  }
  * { margin: 0; padding: 0; box-sizing: border-box; }
  html, body {
    width: 1200px; height: 717px; overflow: hidden;
    background: var(--backdrop);
  }
  .card {
    position: absolute;
    left: 40px; top: 38px;
    width: 1120px; height: 640px;
    background: var(--white);
    box-shadow: 0 6px 18px rgba(0,0,0,0.18);
    overflow: hidden;
  }
  .brand-band {
    position: absolute; left: 0; top: 0;
    width: 100%; height: 440px;
    background: linear-gradient(180deg, var(--band-top), var(--band-bottom));
  }
  .brand-mark {
    position: absolute; left: 60px; top: 120px;
    display: flex; align-items: center; gap: 14px;
  }
  .brand-mark-dot {
    width: 22px; height: 22px; border-radius: 50%;
    background: var(--peach);
    flex: none;
  }
  .brand-mark-name {
    font-family: var(--sans); font-weight: 400;
    font-size: 28px; color: var(--peach);
    white-space: nowrap;
  }
  .company-name {
    position: absolute; left: 430px; top: 58px;
    font-family: var(--serif); font-weight: 700;
    font-size: 52px; letter-spacing: 2px;
    color: var(--white); text-transform: uppercase;
    white-space: nowrap;
  }
  .company-address {
    position: absolute; left: 520px; top: 138px; width: 560px;
    font-family: var(--sans); font-size: 31px; line-height: 38px;
    color: var(--peach); text-align: center;
  }
  .services {
    position: absolute; left: 22px; top: 397px;
    font-family: var(--sans); font-size: 19.5px;
    color: var(--white); white-space: nowrap;
  }
  .contact-person {
    position: absolute; left: 42px; top: 468px;
    font-family: var(--sans); font-size: 32px; line-height: 40px;
    color: var(--ink);
  }
  .contact-lines {
    position: absolute; right: 50px; top: 488px;
    font-family: var(--sans); font-size: 32px; line-height: 42px;
    color: var(--ink); text-align: right;
  }
  .edge-accent {
    position: absolute; left: 0; bottom: 0;
    width: 100%; height: 8px;
    background: var(--accent-green);
  }
</style>
</head>
<body>
  <div class="card">
    <section class="brand-band">
      <div class="brand-mark">
        <span class="brand-mark-dot"></span>
        <span class="brand-mark-name">Harwell Ventures</span>
      </div>
      <h1 class="company-name">Harwell Ventures</h1>
      <p class="company-address">
        4826 Mabry Ln. Suite 417<br>
        Keller, Texas 76109<br>
        www.harwellgrp.example
      </p>
      <p class="services">·Land Development · Residential &amp; Commercial Construction · Commercial Real Estate</p>
    </section>

    <div class="contact-person">
      Dale Wintermoot<br>
      President<br>
      E-mail: dale@harwellgrp.example
    </div>

    <div class="contact-lines">
      Cell: 817-555-0142<br>
      Office: 817-555-0187<br>
      Fax: 817-555-0163
    </div>

    <div class="edge-accent"></div>
  </div>
</body>
</html>
```